Need A Standard Musical Download Website

We are looking for a talented designer to create a unique web design for our startup Music website called Zundo Music.
The website should be responsive and filled with some creative stuffs along with bright colors.

Zundo music is a website loaded with different types of music and capable of downloading the requested music by its users.
There will be categories of music which would be sorted by the genre. They include RnB, Hip-Hop, Afro pop, Pop, Dancehall and Reggae).

DESIGN STYLE/THEME

Creative, trendy, colorful, unique, and easy to use. You have freedom of selecting which ever color suits you. The design must be energetic and attractive.

NAVIGATION

HOME-MUSIC(RnB, Hip hop, Afro pop, POP, dancehall, Reggae)-ARTISTE-NEWS-LOGIN

PAGES REQUIRED
------------
1)Home Page
2)Music

FONTS
GOOGLE FONTS is strongly recommended.

Designers can get inspiration from https://tunevarok.com

Industry/Entity Type

Startup

```html
<!DOCTYPE html>
<html lang="en">
<head>
<meta charset="utf-8">
<title>Zundo Music</title>
<link href="https://fonts.googleapis.com/css2?family=Open+Sans:wght@300;400;600;700&display=swap" rel="stylesheet">
<style>
:root{
  --red:#d93232;
  --red-dark:#c42525;
  --ink:#222;
  --text:#444;
  --muted:#777;
  --line:#d6d6d6;
  --panel:#e4e4e4;
  --card:#f3f3f3;
  --white:#fff;
  --sky-1:#bfe6f2;
  --sky-2:#7fcbe3;
}
*{box-sizing:border-box;margin:0;padding:0}
html,body{width:1200px;height:736px;overflow:hidden;background:var(--white)}
body{font-family:"Open Sans",Arial,sans-serif;color:var(--text);position:relative}
.abs{position:absolute}

.brand{left:132px;top:26px;font-size:39px;font-weight:600;color:var(--red);letter-spacing:-.5px;line-height:1;white-space:nowrap}
.member{right:176px;top:36px;text-align:right;line-height:1.2}
.member small{display:block;font-size:9px;color:var(--text)}
.member strong{display:block;font-size:13px;font-weight:600;color:var(--ink);margin-top:2px}
.member-lock{left:1046px;top:36px}

.nav{left:132px;top:95px;width:935px;height:40px;display:flex;border:1px solid var(--line)}
.nav a{flex:1;display:flex;align-items:center;justify-content:center;font-size:12px;color:var(--text);text-decoration:none;border-left:1px solid var(--line)}
.nav a:first-child{border-left:none}
.nav a.active{background:var(--red);color:var(--white)}

.hero{left:132px;top:138px;width:656px;height:400px;background:linear-gradient(135deg,var(--sky-1) 0%,#a6dcee 45%,var(--sky-2) 100%);overflow:hidden}
.hero-art{position:absolute;left:320px;top:24px;width:320px;height:376px;border-radius:40% 40% 6px 6px;background:radial-gradient(ellipse at 50% 55%,#8a6a4a 0%,#5a4a3e 45%,rgba(90,74,62,0) 72%)}
.hero-title{position:absolute;left:26px;top:106px;width:340px;font-size:20px;font-weight:600;color:var(--ink);line-height:26px}
.hero-text{position:absolute;left:26px;top:164px;width:320px;font-size:15px;line-height:22.5px;color:#333}
.trial{position:absolute;left:26px;top:231px;width:240px;height:68px;background:linear-gradient(180deg,#e23b3b,var(--red-dark));color:var(--white);border-radius:2px;padding:12px 20px;font-size:15px;line-height:22px}
.trial b{font-weight:700;display:block}
.hero-genres{position:absolute;left:26px;top:311px;width:260px;font-size:15px;line-height:22.5px;color:#333}

.side{left:790px;top:138px;width:278px;height:400px;background:linear-gradient(180deg,#e9e9e9,#d8d8d8);overflow:hidden}
.side-intro{position:absolute;left:22px;top:26px;width:245px;font-size:11.5px;line-height:19px;color:var(--text)}
.genres{position:absolute;left:22px;top:92px;display:grid;grid-template-columns:104px 110px;row-gap:8px;list-style:none;font-size:14.5px;color:#333}
.genres li::before{content:"• "}
.phone{position:absolute;left:18px;top:190px;width:120px;height:215px;border:2px solid #cfcfcf;border-bottom:none;border-radius:20px 20px 0 0;background:#f7f7f7}
.phone-dot{position:absolute;left:38px;top:18px;width:4px;height:4px;border-radius:50%;background:#555}
.phone-speaker{position:absolute;left:48px;top:19px;width:22px;height:2px;background:#555;border-radius:2px}
.phone-screen{position:absolute;left:5px;top:36px;width:110px;height:167px;background:linear-gradient(160deg,#cdeaf3,#8fcfe4);border:1px solid #bbb}
.side-brand{position:absolute;left:148px;top:228px;font-size:20px;font-weight:600;color:var(--red);line-height:1;white-space:nowrap;letter-spacing:-.3px}
.side-sub{position:absolute;left:148px;top:257px;font-size:13.5px;line-height:18px;color:var(--ink);white-space:nowrap}
.store{position:absolute;left:150px;width:118px;height:38px;border-radius:2px;display:flex;align-items:center;gap:8px;padding-left:10px;line-height:1.15;white-space:nowrap}
.store small{display:block;font-size:7.5px}
.store b{display:block;font-size:8.5px;font-weight:600}
.store-light{top:284px;background:var(--white);color:#333}
.store-dark{top:330px;background:#222;color:var(--white)}
.store i{width:18px;height:18px;border-radius:50%;flex:none}
.store-light i{background:#9ad0a8}
.store-dark i{background:#ddd}

.cards{left:132px;top:541px;width:936px;height:120px;display:flex;background:var(--card)}
.card{padding:26px 15px 0;border-left:1px solid #dcdcdc}
.card:first-child{border-left:none}
.card h3{font-size:13px;font-weight:400;color:var(--red);margin-bottom:4px;white-space:nowrap}
.card p{font-size:9.5px;line-height:16px;color:var(--muted)}

.foot-nav{left:131px;top:676px;font-size:11px;color:var(--text)}
.foot-nav span{margin:0 8px;color:#666}
.copy{left:131px;top:701px;font-size:11px;color:var(--text)}
.social{left:976px;top:684px;display:flex;gap:7px}
.social i{width:26px;height:26px;border-radius:50%}
.s1{background:#3b5ea8}.s2{background:#29a9e0}.s3{background:#e62b26}
</style>
</head>
<body>

<div class="abs brand">Zundo Music</div>
<div class="abs member"><small>Already a Member?</small><strong>LOGIN</strong></div>
<svg class="abs member-lock" width="22" height="27" viewBox="0 0 22 27" aria-hidden="true">
  <path d="M5 12V8a6 6 0 0 1 12 0v4" fill="none" stroke="#666" stroke-width="1.4"/>
  <rect x="1" y="12" width="20" height="14" rx="1.5" fill="none" stroke="#666" stroke-width="1.4"/>
  <path d="M3 20l4-4M7 22l6-6M12 22l6-6M17 22l3-3" stroke="#666" stroke-width="1"/>
</svg>

<nav class="abs nav">
  <a class="active" href="#">HOME</a>
  <a href="#">MUSIC</a>
  <a href="#">ARTISTE</a>
  <a href="#">NEWS</a>
  <a href="#">LOGIN</a>
</nav>

<section class="abs hero">
  <div class="hero-art" role="img" aria-label="A stacked pile of musical instruments and radios: boombox, guitars, saxophone, accordion, trumpet and banjo"></div>
  <h1 class="hero-title">Aenean odio turpis, maximus et dolor et, feugiat iaculis augue.</h1>
  <p class="hero-text">Nullam rutrum hendrerit leo, in hendrerit lectus. Ut blandit, arcu vel fringilla sollicitudin, erat quam aliquet odio, non.</p>
  <div class="trial">Download Up To<b>25 Free Songs* With Trial</b></div>
  <p class="hero-genres">RnB, Hip-Hop, Afro pop, Pop, Dancehall and Reggae</p>
</section>

<aside class="abs side">
  <p class="side-intro">Nam enim sem, rutrum vel mauris et, facilisis facilisis augue. In aliquam tristique placerat. Sed et ex nisi.</p>
  <ul class="genres">
    <li>RNB</li><li>POP</li>
    <li>HIP-HOP</li><li>DANCEHALL</li>
    <li>AFRO POP</li><li>REGGAE</li>
  </ul>
  <div class="phone">
    <span class="phone-dot"></span><span class="phone-speaker"></span>
    <div class="phone-screen" role="img" aria-label="App screen showing the stacked instruments artwork"></div>
  </div>
  <div class="side-brand">Zundo Music</div>
  <div class="side-sub">Download Here</div>
  <div class="store store-light"><i></i><span><small>Download it from</small><b>GRIDPLAY</b></span></div>
  <div class="store store-dark"><i></i><span><small>Download it from</small><b>APPORA STORE</b></span></div>
</aside>

<section class="abs cards">
  <article class="card" style="width:231px">
    <h3>Donec varius mi vitae</h3>
    <p>Mauris sem ante, suscipit eu sagittis eget, eleifend sed nunc. Nunc ut rhoncus mauris. Sed a erat aliquet, ultrices mauris</p>
  </article>
  <article class="card" style="width:235px">
    <h3>Maecenas gravida risus lorem</h3>
    <p>Mauris sem ante, suscipit eu sagittis eget, eleifend sed nunc. Nunc ut rhoncus mauris. Sed a erat aliquet, ultrices mauris</p>
  </article>
  <article class="card" style="width:239px">
    <h3>Nulla id consectetur</h3>
    <p>Mauris sem ante, suscipit eu sagittis eget, eleifend sed nunc. Nunc ut rhoncus mauris. Sed a erat aliquet, ultrices mauris</p>
  </article>
  <article class="card" style="width:231px">
    <h3>Sed a erat aliquet</h3>
    <p>Mauris sem ante, suscipit eu sagittis eget, eleifend sed nunc. Nunc ut rhoncus mauris. Sed a erat aliquet, ultrices mauris</p>
  </article>
</section>

<div class="abs foot-nav">Home<span>|</span>Music<span>|</span>Artiste<span>|</span>News<span>|</span>Login</div>
<div class="abs copy">Copyright &copy; 2017 Company name. All rights reserved.</div>
<div class="abs social"><i class="s1"></i><i class="s2"></i><i class="s3"></i></div>

</body>
</html>
```